Stationary Design

Harbor Stagecraft Collective, Inc
27410 Marlowe Blvd Ste 4, Santa Fe Springs, CA 90512
Office: 213-584-2760 Email: admin@hsccrew.example

Industry/Entity Type

Entertainment

Colors
0054AA
0677BA
7BADD7
CADEEF
E8F1F8

```html
<!DOCTYPE html>
<html lang="en">
<head>
<meta charset="utf-8">
<title>Harbor Stagecraft Collective — Business Card</title>
<link href="https://fonts.googleapis.com/css2?family=Arimo:wght@400;700&display=swap" rel="stylesheet">
<style>
  :root {
    --brand-blue: #0054aa;
    --brand-mid: #0677ba;
    --brand-light: #7badd7;
    --brand-pale: #cadeef;
    --brand-mist: #e8f1f8;
    --night-deep: #0d1a3f;
    --night-mid: #1f3a80;
    --ink-gray: #555a60;
    --rule-gray: #a9adb2;
    --card-white: #ffffff;
    --backdrop: #e6e8eb;
  }
  * { box-sizing: border-box; margin: 0; padding: 0; }
  html, body { width: 1200px; height: 689px; overflow: hidden; }
  body {
    background: var(--backdrop);
    font-family: "Arimo", Arial, sans-serif;
    position: relative;
  }
  .card {
    position: absolute;
    top: 196px;
    width: 520px;
    height: 297px;
    border-radius: 18px;
    overflow: hidden;
    box-shadow: 0 10px 28px rgba(0,0,0,.18);
  }
  /* Back face */
  .card-back { left: 50px; }
  .skyline-photo {
    position: absolute; inset: 0;
    background:
      linear-gradient(180deg, var(--night-mid) 0%, #1c2f6a 35%, #223a7a 55%, #3a4a6a 75%, #3b3426 100%);
  }
  .back-brand {
    position: absolute; top: 26px; right: 30px;
    display: flex; flex-direction: column; align-items: flex-end; gap: 8px;
    color: var(--card-white);
  }
  .back-brand .brand-row { display: flex; align-items: center; gap: 8px; }
  .brand-dot {
    width: 26px; height: 26px; border-radius: 50%;
    background: var(--card-white);
  }
  .back-brand .brand-name { font-size: 15px; font-weight: 700; letter-spacing: .5px; }
  .back-brand .brand-web { font-size: 13px; }

  /* Front face */
  .card-front { left: 630px; background: var(--card-white); }
  .front-logo {
    position: absolute; left: 30px; top: 104px; width: 210px;
    display: flex; flex-direction: column; align-items: center; gap: 10px;
  }
  .front-logo .brand-dot { width: 48px; height: 48px; background: var(--brand-blue); }
  .front-logo .brand-name {
    color: var(--brand-blue); font-size: 17px; font-weight: 700;
    text-align: center; line-height: 1.2; letter-spacing: .4px;
  }
  .divider {
    position: absolute; left: 262px; top: 30px; width: 1px; height: 200px;
    background: linear-gradient(180deg, transparent, var(--rule-gray) 20%, var(--rule-gray) 80%, transparent);
  }
  .contact {
    position: absolute; left: 282px; top: 40px; width: 225px;
    color: var(--ink-gray); font-size: 11.5px; line-height: 1.35;
  }
  .contact .person-name { color: var(--brand-blue); font-size: 20px; font-weight: 700; letter-spacing: .3px; }
  .contact .person-role { font-size: 11px; margin-bottom: 12px; }
  .contact .address { margin-bottom: 10px; }
  .contact-line { display: flex; align-items: center; gap: 7px; }
  .contact-line svg { width: 11px; height: 11px; flex: none; fill: var(--brand-blue); }
  .edge-rule {
    position: absolute; left: 0; right: 0; bottom: 16px; height: 2px;
    background: var(--rule-gray);
  }
  .edge-band {
    position: absolute; left: 0; right: 0; bottom: 0; height: 13px;
    background: var(--brand-blue);
  }
</style>
</head>
<body>

<section class="card card-back">
  <div class="skyline-photo" role="img" aria-label="Night-time city skyline photo with lit towers under a deep blue sky"></div>
  <div class="back-brand">
    <div class="brand-row">
      <span class="brand-dot"></span>
      <span class="brand-name">HARBOR STAGECRAFT COLLECTIVE</span>
    </div>
    <span class="brand-web">www.hsccrew.example</span>
  </div>
</section>

<section class="card card-front">
  <div class="front-logo">
    <span class="brand-dot"></span>
    <span class="brand-name">HARBOR STAGECRAFT<br>COLLECTIVE</span>
  </div>

  <div class="divider"></div>

  <div class="contact">
    <div class="person-name">DANA WHITLOW</div>
    <div class="person-role">President</div>
    <div class="address">
      Harbor Stagecraft Collective, Inc<br>
      27410 Marlowe Blvd Ste 4,<br>
      Santa Fe Springs, CA 90512
    </div>
    <div class="contact-line">
      <svg viewBox="0 0 24 24"><path d="M6.6 10.8a15 15 0 0 0 6.6 6.6l2.2-2.2c.3-.3.7-.4 1-.2 1.1.4 2.3.6 3.6.6.6 0 1 .4 1 1V20c0 .6-.4 1-1 1A17 17 0 0 1 3 4c0-.6.4-1 1-1h3.5c.6 0 1 .4 1 1 0 1.3.2 2.5.6 3.6.1.3 0 .7-.2 1z"/></svg>
      <span>213-584-2760</span>
    </div>
    <div class="contact-line">
      <svg viewBox="0 0 24 24"><path d="M2 5h20v14H2zm2 2v.5l8 5 8-5V7zm0 3v7h16v-7l-8 5z"/></svg>
      <span>admin@hsccrew.example</span>
    </div>
    <div class="contact-line">
      <svg viewBox="0 0 24 24"><circle cx="12" cy="12" r="10"/></svg>
      <span>www.hsccrew.example</span>
    </div>
  </div>

  <div class="edge-rule"></div>
  <div class="edge-band"></div>
</section>

</body>
</html>
```